I just launched a new website and would like a new design for my company facebook page. Our website is www.marlowprintworks.com and our current facebook page can be found at http://www.facebook.com/pages/Marlow-Printworks/584190627413
We are a customer friendly digital printing company that specializes in very fast turnaround in the New York City market.

```html
<!DOCTYPE html>
<html lang="en">
<head>
<meta charset="utf-8">
<title>Marlow Printworks – Facebook Cover</title>
<link href="https://fonts.googleapis.com/css2?family=Black+Ops+One&family=Architects+Daughter&family=PT+Serif&family=Open+Sans:wght@700&display=swap" rel="stylesheet">
<style>
  :root {
    --sky-top: #1d96da;
    --sky-bottom: #0b5aa5;
    --skyline-tone: #0a4f95;
    --accent-orange: #f7941d;
    --badge-ink: #6b3d0a;
    --headline: #ffffff;
    --tagline: #f7941d;
    --button-top: #3a3a3a;
    --button-bottom: #1c1c1c;
    --button-edge: #5d5d5d;
    --button-text: #ffffff;
  }
  * { box-sizing: border-box; margin: 0; padding: 0; }
  html, body { width: 1200px; height: 443px; overflow: hidden; background: #ffffff; }
  .cover {
    position: relative;
    width: 1200px;
    height: 443px;
    overflow: hidden;
    background: linear-gradient(180deg, var(--sky-top) 0%, #1583cb 55%, var(--sky-bottom) 100%);
  }
  .skyline {
    position: absolute;
    left: 0; right: 0;
    top: 170px; bottom: 13px;
    background: linear-gradient(180deg, rgba(10,79,149,0) 0%, rgba(10,79,149,0.55) 35%, var(--skyline-tone) 100%);
  }
  .footer-band {
    position: absolute;
    left: 0; right: 0; bottom: 0;
    height: 13px;
    background: var(--accent-orange);
  }
  .call-badge {
    position: absolute;
    left: 31px; top: 0;
    width: 389px; height: 65px;
    background: var(--accent-orange);
    box-shadow: 0 2px 4px rgba(0,0,0,0.25);
  }
  .call-badge svg { position: absolute; left: 36px; top: 12px; }
  .call-label {
    position: absolute; left: 90px; top: 8px;
    font: 12px "PT Serif", serif;
    color: var(--badge-ink);
    letter-spacing: 0.5px;
  }
  .call-number {
    position: absolute; left: 90px; top: 22px;
    font: 29px/1 "PT Serif", serif;
    color: var(--badge-ink);
    letter-spacing: 0.5px;
  }
  .pitch {
    position: absolute;
    right: 40px;
    text-align: right;
  }
  .pitch h2 {
    font: 400 40px/1 "Black Ops One", sans-serif;
    color: var(--headline);
    letter-spacing: 1px;
    text-shadow: 2px 2px 0 rgba(5,45,90,0.7);
  }
  .pitch p {
    margin-top: 2px;
    font: 19px/1.1 "Architects Daughter", cursive;
    color: var(--tagline);
  }
  .pitch-quality { top: 54px; }
  .pitch-service { top: 155px; }
  .pitch-speed { top: 250px; }
  .contact-button {
    position: absolute;
    top: 364px;
    height: 42px;
    display: flex;
    align-items: center;
    gap: 12px;
    padding: 0 16px;
    border-radius: 4px;
    border: 1px solid var(--button-edge);
    background: linear-gradient(180deg, var(--button-top), var(--button-bottom));
    box-shadow: 0 2px 3px rgba(0,0,0,0.35);
    font: 700 16px "Open Sans", sans-serif;
    color: var(--button-text);
    white-space: nowrap;
  }
  .contact-web { left: 367px; width: 299px; }
  .contact-mail { left: 680px; width: 285px; }
  .contact-social { left: 983px; width: 182px; }
  .dot {
    width: 22px; height: 22px;
    border-radius: 50%;
    background: var(--button-text);
    flex: none;
  }
</style>
</head>
<body>
<div class="cover">
  <div class="skyline" role="img" aria-label="Silhouette of the New York City skyline with the Statue of Liberty"></div>
  <div class="footer-band"></div>

  <div class="call-badge">
    <svg width="40" height="40" viewBox="0 0 40 40" aria-hidden="true">
      <circle cx="20" cy="20" r="17" fill="none" stroke="#6b3d0a" stroke-width="3"/>
      <path d="M14 11c1.5-1 3-.5 3.5.7l1.3 3c.4 1-.2 1.8-1 2.4l-1 .7c.8 2.3 2.6 4.2 4.8 5l.8-1c.6-.8 1.4-1.3 2.4-.9l3 1.3c1.2.5 1.6 2 .7 3.4-1.2 1.9-3.4 2.6-5.6 1.8-5.3-2-9-5.8-10.8-11-.6-2 .1-3.9 1.9-5.4z" fill="#6b3d0a"/>
    </svg>
    <div class="call-label">CALL US</div>
    <div class="call-number">1.212.555.0147</div>
  </div>

  <section class="pitch pitch-quality">
    <h2>HIGH QUALITY PRINTING</h2>
    <p>New York City's specialist in digital, offset and large format printing</p>
  </section>
  <section class="pitch pitch-service">
    <h2>FRIENDLY SERVICE</h2>
    <p>Call (or email) us now to speak with a customer service representative</p>
  </section>
  <section class="pitch pitch-speed">
    <h2>FAST TURNAROUND</h2>
    <p>on demand printing when you need it</p>
  </section>

  <div class="contact-button contact-web"><span class="dot"></span>www.marlowprintworks.com</div>
  <div class="contact-button contact-mail">
    <svg width="26" height="18" viewBox="0 0 26 18" aria-hidden="true">
      <rect x="1" y="1" width="24" height="16" fill="none" stroke="#ffffff" stroke-width="2"/>
      <path d="M1 1l12 9 12-9" fill="none" stroke="#ffffff" stroke-width="2"/>
    </svg>
    Youremail@domain.com
  </div>
  <div class="contact-button contact-social"><span class="dot"></span>@my_twitter</div>
</div>
</body>
</html>
```